Business software developers new website

We need to redesign our website. Our current website is http://www.plumvista.net/index.html, which is outdated and needs a new look. We moved out from web design and have concentrated more on the back end of the systems, for example, system support and security and cloud-based applications. Our major clients include both private and government sectors. We would like to see some designs that are all in one page, simple and clean. Prefer illustrator or obstructed images instead of real-life photos. Must look futuristic yet friendly. Attached the new logo for your references and good luck.

Target Market(s)

Medium to big company for their IT or data management. Either improve or upgrade their current system.

Industry/Entity Type

Business Software

Number of Pages Required

1 page

Colors

Designer to choose colors to be used in the design.

Requirements
Must have
• Simple and clean. Individual assets must be provided in the correct size and format(png or jpeg). Prefer Goggle fonts. Even though the logo color is red, grey and black, still prefer some modern colors that go well with red. When design, must consider the possibility to convert it into responsive.
Nice to have
• White background
Should not have
• real life photos, no slider

```html
<!DOCTYPE html>
<html lang="en">
<head>
<meta charset="utf-8">
<title>Plumvista – System Security &amp; Cloud Applications</title>
<link href="https://fonts.googleapis.com/css2?family=Dosis:wght@500;600;700;800&family=Open+Sans:wght@400;600;700&display=swap" rel="stylesheet">
<style>
:root{
  --red:#f0141e;
  --blue:#0c0ca0;
  --ink:#1b1b2a;
  --text:#6b6b78;
  --muted:#9a9aa6;
  --pale:#fdf2f2;
  --white:#ffffff;
  --line:#e6e6ee;
}
*{box-sizing:border-box;margin:0;padding:0}
html,body{width:1200px;height:4675px;overflow:hidden}
body{font-family:"Open Sans",Arial,sans-serif;color:var(--text);background:var(--white);position:relative;font-size:12px;line-height:1.6}
h1,h2,h3,h4{font-family:"Dosis","Trebuchet MS",sans-serif;color:var(--ink)}
.section{position:absolute;left:0;width:1200px}
.btn{display:inline-block;font-family:"Dosis",sans-serif;font-weight:700;font-size:11px;letter-spacing:.5px;text-transform:uppercase;color:#fff;background:var(--red);padding:6px 14px;border-radius:2px;line-height:1.4}
.sec-title{position:absolute;left:0;width:1200px;text-align:center;font-size:30px;font-weight:700;line-height:1.2}
.sec-sub{position:absolute;left:390px;width:420px;text-align:center;font-size:11px;color:var(--muted);line-height:1.7}
.divider{position:absolute;left:599px;width:1px;height:40px;background:var(--line)}

/* header */
.site-header{top:0;height:95px}
.wordmark{position:absolute;font-family:"Dosis",sans-serif;font-weight:700;font-size:28px;line-height:1;color:var(--ink)}
.nav{position:absolute;left:425px;top:26px;display:flex;gap:26px;align-items:center;font-family:"Dosis",sans-serif;font-weight:700;font-size:11px;color:var(--ink);letter-spacing:.3px}
.nav .active{color:var(--red)}
.nav .btn{padding:4px 12px}
.nav .btn.login{background:var(--blue)}

/* hero */
.hero{top:95px;height:429px}
.hero h1{position:absolute;left:160px;top:140px;width:470px;font-size:23px;font-weight:800;line-height:1.3}
.hero p{position:absolute;left:160px;top:202px;width:390px;font-size:11px}
.hero .btn{position:absolute;left:160px;top:258px}
.hero-art{position:absolute;left:760px;top:60px;width:270px;height:280px;border-radius:8px;background:linear-gradient(180deg,#eef0f5,#d8dbe6)}

/* stats + why */
.why{top:524px;height:723px;background:var(--blue)}
.stat{position:absolute;top:-32px;height:197px;background:#fff;border-radius:4px;box-shadow:0 6px 20px rgba(0,0,0,.15);padding:22px 18px 0 90px}
.stat svg{position:absolute;left:26px;top:30px}
.stat small{font-size:9px;color:var(--muted);display:block;line-height:1.2}
.stat .num{font-family:"Dosis",sans-serif;font-weight:800;font-size:32px;color:var(--ink);line-height:1.05}
.stat .lbl{font-size:11px;color:var(--ink);font-weight:600;line-height:1.3}
.stat-text{position:absolute;left:26px;right:24px;top:110px;font-size:10px;line-height:1.6;color:var(--text)}
.why .sec-title{top:268px;color:#fff}
.why .sec-sub{top:312px;color:#cfd0f5}
.why .divider{top:215px;background:rgba(255,255,255,.35)}
.feature{position:absolute;width:260px;color:#d5d6f7;font-size:10px;line-height:1.6}
.feature h4{color:#fff;font-size:15px;font-weight:700;margin-bottom:2px}
.feature svg{position:absolute;top:2px}
.feature.left{left:160px;text-align:right;padding-right:56px}
.feature.left svg{right:6px}
.feature.right{left:757px;padding-left:60px}
.feature.right svg{left:0}
.why-art{position:absolute;left:492px;top:380px;width:219px;height:296px;border-radius:8px;background:linear-gradient(180deg,#2a2ab8,#1a1aa4)}

/* offer */
.offer{top:1247px;height:801px;background:var(--pale)}
.offer .divider{top:45px}
.offer .sec-title{top:105px}
.offer .sec-sub{top:150px}
.card{position:absolute;width:275px;height:250px;text-align:center;padding-top:30px;border-radius:3px}
.card.raised{background:#fff;box-shadow:0 6px 24px rgba(0,0,0,.12)}
.card h3{font-size:16px;font-weight:700;margin:12px 0 10px;line-height:1.2}
.card p{font-size:10px;width:200px;margin:0 auto;line-height:1.6}
.card .more{display:block;margin-top:14px;font-family:"Dosis",sans-serif;font-weight:700;font-size:11px;color:var(--ink)}

/* about */
.about{top:2048px;height:436px}
.about-video{position:absolute;left:162px;top:81px;width:424px;height:271px;background:linear-gradient(180deg,#e3ebf4,#c9d6e6)}
.about-video .play{position:absolute;left:188px;top:105px;width:46px;height:46px;border-radius:50%;background:#fff;box-shadow:0 2px 8px rgba(0,0,0,.2)}
.about-video .bar{position:absolute;left:0;bottom:0;width:100%;height:30px;background:rgba(40,50,70,.85)}
.about h2{position:absolute;left:686px;top:80px;font-size:24px;font-weight:700;line-height:1.2}
.about p{position:absolute;left:686px;width:355px;font-size:10px;line-height:1.75}

/* testimonials */
.testimonials{top:2484px;height:518px;background:linear-gradient(180deg,#1010a4 0%,#5a1a8a 45%,#f0141e 100%)}
.testimonials .divider{top:55px;background:rgba(255,255,255,.35)}
.testimonials .sec-title{top:100px;color:#fff}
.quote-card{position:absolute;left:312px;top:172px;width:654px;height:243px;background:#fff;text-align:center;padding:90px 50px 0}
.avatar{position:absolute;width:54px;height:54px;border-radius:50%;background:#cfcfd6}
.quote-card .avatar{left:300px;top:22px}
.quote-card p{font-size:11px;line-height:1.7}
.quote-card .client{display:block;margin-top:14px;font-family:"Dosis",sans-serif;font-weight:700;font-size:14px;color:var(--red);line-height:1.3}
.quote-card .role{font-size:9px;font-weight:700;color:var(--ink)}
.arrow{position:absolute;top:285px}
.dots{position:absolute;left:570px;top:422px;display:flex;gap:6px}
.dots span{width:12px;height:12px;background:var(--red)}
.dots span.on{background:#fff}

/* blog */
.blog{top:3002px;height:660px;background:var(--pale)}
.blog .sec-title{top:48px}
.blog .sec-sub{top:92px}
.post{position:absolute;top:168px;width:282px;height:405px;background:#fff;box-shadow:0 4px 16px rgba(0,0,0,.08)}
.post .thumb{height:187px}
.post .avatar{left:22px;top:163px;width:46px;height:46px;border:3px solid #fff}
.post h3{position:absolute;left:22px;top:225px;width:240px;font-size:15px;font-weight:700;line-height:1.25}
.post p{position:absolute;left:22px;top:272px;width:230px;font-size:10px;line-height:1.6}
.post .date{position:absolute;left:22px;top:338px;font-size:10px;color:var(--ink);display:flex;align-items:center;gap:8px}
.blog .btn{position:absolute;left:522px;top:625px}

/* contact */
.contact{top:3662px;height:686px}
.contact .sec-title{top:90px}
.contact .sec-sub{top:134px}
.red-band{position:absolute;left:0;top:468px;width:1200px;height:218px;background:var(--red)}
.form{position:absolute;left:162px;top:219px;width:580px;height:311px;background:#fff;box-shadow:0 4px 20px rgba(0,0,0,.1)}
.field{position:absolute;height:32px;border:1px solid var(--line);font-size:10px;color:var(--muted);padding:8px 10px;line-height:1.4}
.send{position:absolute;left:35px;top:262px;width:510px;height:30px;border-radius:15px;background:#111;color:#fff;text-align:center;font-family:"Dosis",sans-serif;font-weight:700;font-size:11px;line-height:30px}
.map{position:absolute;left:760px;top:219px;width:284px;height:311px;background:linear-gradient(135deg,#e8eef3,#cfdde8)}
.map .tab{position:absolute;top:0;height:24px;background:#fff;font-size:10px;color:var(--ink);padding:4px 10px}
.info{position:absolute;top:585px;width:270px;padding-left:58px;color:#fff;font-size:10px;line-height:1.6}
.info h4{color:#fff;font-size:13px;font-weight:700;line-height:1.3}
.info .ring{position:absolute;left:0;top:2px;width:40px;height:40px;border:2px solid #fff;border-radius:50%;display:flex;align-items:center;justify-content:center}

/* footer */
.footer{top:4348px;height:327px;background:#fff}
.footer .wordmark{left:160px;top:78px}
.footer .about-text{position:absolute;left:160px;top:118px;width:270px;font-size:10px;line-height:1.7}
.social{position:absolute;left:160px;top:198px;display:flex;gap:12px}
.social span{width:26px;height:26px;border:1.5px solid var(--red);border-radius:50%}
.fcol{position:absolute;top:74px;font-size:10px}
.fcol h4{font-size:13px;font-weight:800;margin-bottom:10px;letter-spacing:.3px;line-height:1.2}
.fcol li{list-style:none;line-height:2;padding-left:10px;position:relative}
.fcol li::before{content:"";position:absolute;left:0;top:9px;width:4px;height:4px;background:var(--red)}
.fcol li.current{color:var(--red)}
.news-input{position:absolute;left:835px;top:160px;width:205px;height:28px;border:1px solid var(--line);font-size:10px;color:var(--muted);padding:6px 10px;line-height:1.4}
.bottom-bar{position:absolute;left:0;top:287px;width:1200px;height:40px;border-top:1px solid var(--line);font-size:9px;color:var(--text)}
.bottom-bar span{position:absolute;left:160px;top:13px}
</style>
</head>
<body>

<header class="section site-header">
  <div class="wordmark" style="left:160px;top:22px">Plumvista</div>
  <nav class="nav">
    <span class="active">HOME</span><span>OUR SERVICES</span><span>ABOUT</span><span>FEATURES</span><span>OUR CLIENTS</span><span>CONTACT</span>
    <span class="btn">Sign Up</span><span class="btn login">Login</span>
  </nav>
</header>

<section class="section hero">
  <h1>Provide system security &amp; cloud based applications services</h1>
  <p>Lorem ipsum dolor sit amet, consectetur adipiscing elit, sed do eiusmod tempor incididunt ut labore et dolore magna aliqua.</p>
  <span class="btn">Learn More &#8250;</span>
  <div class="hero-art" role="img" aria-label="Illustration of a cloud with a padlock above a laptop, monitor, tablet and phone"></div>
</section>

<section class="section why">
  <div class="stat" style="left:162px;width:274px">
    <svg width="40" height="40" viewBox="0 0 40 40" fill="none" stroke="#f0141e" stroke-width="2"><path d="M10 24a7 7 0 0 1 1-14 9 9 0 0 1 17 2 6 6 0 0 1 1 12z"/><path d="M14 24v8M20 24v10M26 24v8"/></svg>
    <small>More than</small><div class="num">200+</div><div class="lbl">Dedicated Servers</div>
    <p class="stat-text">Lorem ipsum dolor sit amet, consectetur adipiscing elit, sed do eiusmod tempor incididunt ut labore et dolore magna aliqua.</p>
  </div>
  <div class="stat" style="left:461px;width:275px">
    <svg width="40" height="40" viewBox="0 0 40 40"><circle cx="20" cy="20" r="17" fill="#f0141e"/><circle cx="14" cy="16" r="2" fill="#fff"/><circle cx="26" cy="16" r="2" fill="#fff"/><path d="M12 23q8 9 16 0" stroke="#fff" stroke-width="2.5" fill="none"/></svg>
    <small>Up to</small><div class="num">99%</div><div class="lbl">Satisfied Customers</div>
    <p class="stat-text">Lorem ipsum dolor sit amet, consectetur adipiscing elit, sed do eiusmod tempor incididunt ut labore et dolore magna aliqua.</p>
  </div>
  <div class="stat" style="left:760px;width:275px">
    <svg width="40" height="40" viewBox="0 0 40 40" fill="#f0141e"><path d="M20 4 36 12 20 20 4 12z"/><path d="M4 19l16 8 16-8v5l-16 8-16-8z"/><path d="M4 27l16 8 16-8v4l-16 8-16-8z" opacity=".7"/></svg>
    <small>Up to</small><div class="num">400+</div><div class="lbl">CMS Installations</div>
    <p class="stat-text">Lorem ipsum dolor sit amet, consectetur adipiscing elit, sed do eiusmod tempor incididunt ut labore et dolore magna aliqua.</p>
  </div>

  <div class="divider"></div>
  <h2 class="sec-title">Why Choose Us</h2>
  <p class="sec-sub">Duis aute irure dolor in reprehenderit in voluptate velit esse cillum dolore eu fugiat nulla pariatur. Excepteur sint occaecat cupidatat non proident.</p>

  <div class="feature left" style="top:405px">
    <svg width="36" height="36" viewBox="0 0 36 36" fill="none" stroke="#fff" stroke-width="2"><rect x="5" y="8" width="26" height="18" rx="2"/><path d="M12 31h12M18 26v5"/></svg>
    <h4>High-Quality Hardware</h4>Lorem ipsum dolor sit amet, consectetur adipiscing elit, sed do eiusmod
  </div>
  <div class="feature left" style="top:505px">
    <svg width="36" height="36" viewBox="0 0 36 36" fill="none" stroke="#fff" stroke-width="2"><path d="M29 18a11 11 0 1 1-3-7.5"/><path d="M29 6v6h-6"/></svg>
    <h4>Instant Software Updates</h4>Lorem ipsum dolor sit amet, consectetur adipiscing elit, sed do eiusmod
  </div>
  <div class="feature left" style="top:614px">
    <svg width="36" height="36" viewBox="0 0 36 36" fill="none" stroke="#fff" stroke-width="2"><ellipse cx="18" cy="9" rx="11" ry="4"/><path d="M7 9v18c0 2 5 4 11 4s11-2 11-4V9M7 18c0 2 5 4 11 4s11-2 11-4"/></svg>
    <h4>Server Level Protection</h4>Lorem ipsum dolor sit amet, consectetur adipiscing elit, sed do eiusmod
  </div>

  <div class="why-art" role="img" aria-label="Isometric illustration of server racks linked to a cloud"></div>

  <div class="feature right" style="top:405px">
    <svg width="36" height="36" viewBox="0 0 36 36" fill="none" stroke="#fff" stroke-width="2"><path d="M7 20v-3a11 11 0 0 1 22 0v3"/><rect x="5" y="19" width="6" height="9" rx="2"/><rect x="25" y="19" width="6" height="9" rx="2"/></svg>
    <h4>Dedicated 24/7 Support</h4>Lorem ipsum dolor sit amet, consectetur adipiscing elit, sed do eiusmod
  </div>
  <div class="feature right" style="top:505px">
    <svg width="36" height="36" viewBox="0 0 36 36" fill="#fff"><path d="M5 16h6v14H5zM13 16l6-10c3 0 4 2 3 5l-1 4h8c2 0 3 2 2 4l-3 9c-1 2-2 2-4 2H13z"/></svg>
    <h4>Trusted Cloud Based Services</h4>Lorem ipsum dolor sit amet, consectetur adipiscing elit, sed do eiusmod
  </div>
  <div class="feature right" style="top:614px">
    <svg width="36" height="36" viewBox="0 0 36 36" fill="none" stroke="#fff" stroke-width="2"><path d="M9 26a7 7 0 0 1 1-13 9 9 0 0 1 17 2 6 6 0 0 1 0 11z"/></svg>
    <h4>Cloud Edge Integration</h4>Lorem ipsum dolor sit amet, consectetur adipiscing elit, sed do eiusmod
  </div>
</section>

<section class="section offer">
  <div class="divider"></div>
  <h2 class="sec-title">What We Offer</h2>
  <p class="sec-sub">Duis aute irure dolor in reprehenderit in voluptate velit esse cillum dolore eu fugiat nulla pariatur. Excepteur sint occaecat cupidatat non proident.</p>

  <div class="card raised" style="left:162px;top:230px">
    <svg width="40" height="40" viewBox="0 0 40 40" fill="none" stroke="#f0141e" stroke-width="2"><rect x="6" y="7" width="22" height="17" rx="1"/><path d="M12 30h10M17 24v6"/><rect x="30" y="10" width="6" height="20"/></svg>
    <h3>System Support</h3><p>Nemo enim ipsam voluptatem quia voluptas sit aspernatur aut odit aut fugit, sed quia consequuntur magni dolores</p><span class="more">Read More</span>
  </div>
  <div class="card" style="left:462px;top:230px">
    <svg width="40" height="40" viewBox="0 0 40 40" fill="none" stroke="#f0141e" stroke-width="2"><path d="M11 24a7 7 0 0 1 1-13 9 9 0 0 1 17 2 6 6 0 0 1 0 11z"/><path d="M20 24v10M13 34h14"/></svg>
    <h3>Dedicated Servers</h3><p>Nemo enim ipsam voluptatem quia voluptas sit aspernatur aut odit aut fugit, sed quia consequuntur magni dolores</p><span class="more">Read More</span>
  </div>
  <div class="card" style="left:760px;top:230px">
    <svg width="40" height="40" viewBox="0 0 40 40" fill="none" stroke="#f0141e" stroke-width="2"><path d="M10 26a7 7 0 0 1 1-13 9 9 0 0 1 17 2 6 6 0 0 1 1 11z"/><path d="M15 26v6M20 26v8M25 26v6"/></svg>
    <h3>Cloud Services</h3><p>Nemo enim ipsam voluptatem quia voluptas sit aspernatur aut odit aut fugit, sed quia consequuntur magni dolores</p><span class="more">Read More</span>
  </div>
  <div class="card" style="left:162px;top:510px">
    <svg width="40" height="40" viewBox="0 0 40 40" fill="none" stroke="#f0141e" stroke-width="2"><path d="M9 28a12 12 0 1 1 22 0"/><path d="M20 28l6-9"/><circle cx="20" cy="28" r="2"/></svg>
    <h3>Security</h3><p>Nemo enim ipsam voluptatem quia voluptas sit aspernatur aut odit aut fugit, sed quia consequuntur magni dolores</p><span class="more">Read More</span>
  </div>
  <div class="card" style="left:462px;top:510px">
    <svg width="40" height="40" viewBox="0 0 40 40" fill="none" stroke="#f0141e" stroke-width="2"><path d="M31 20a11 11 0 1 1-3-7.5"/><path d="M31 7v6h-6"/><path d="M20 14v7l4 3"/></svg>
    <h3>Backup &amp; Restore</h3><p>Nemo enim ipsam voluptatem quia voluptas sit aspernatur aut odit aut fugit, sed quia consequuntur magni dolores</p><span class="more">Read More</span>
  </div>
  <div class="card" style="left:760px;top:510px">
    <svg width="40" height="40" viewBox="0 0 40 40" fill="none" stroke="#f0141e" stroke-width="2"><rect x="15" y="5" width="10" height="8"/><rect x="4" y="27" width="10" height="8"/><rect x="26" y="27" width="10" height="8"/><path d="M20 13v7M9 27v-7h22v7"/></svg>
    <h3>Network</h3><p>Nemo enim ipsam voluptatem quia voluptas sit aspernatur aut odit aut fugit, sed quia consequuntur magni dolores</p><span class="more">Read More</span>
  </div>
</section>

<section class="section about">
  <div class="about-video" role="img" aria-label="Video still illustrating two people securing a cloud with a padlock">
    <div class="play"></div><div class="bar"></div>
  </div>
  <h2>About Plumvista</h2>
  <p style="top:128px">Plumvista is an Australian based software company that provides first class technology solutions and professional software for clients worldwide. Our team is based on quality, stable, scalable and technical support services, giving clients a trusted partner for their systems and data management needs. Our programming specialists focus on delivering solutions for small and large enterprises across government and private sectors.</p>
  <p style="top:272px">Providing the best quality of service and assistance of support we take pride in giving customers the software they need, the choice, over time to suit their needs.</p>
</section>

<section class="section testimonials">
  <div class="divider"></div>
  <h2 class="sec-title">Testimonials</h2>
  <svg class="arrow" style="left:262px" width="14" height="16" viewBox="0 0 14 16"><path d="M10 2 4 8l6 6" stroke="#fff" stroke-width="2.5" fill="none"/></svg>
  <div class="quote-card">
    <div class="avatar" role="img" aria-label="Client portrait placeholder"></div>
    <p>Duis aute irure dolor in reprehenderit in voluptate velit esse cillum dolore eu fugiat nulla pariatur. Excepteur sint occaecat cupidatat non proident, sunt in culpa qui officia deserunt mollit anim id est laborum. Sed ut perspiciatis unde omnis iste natus error sit voluptatem.</p>
    <span class="client">Client Name</span><span class="role">Profession</span>
  </div>
  <svg class="arrow" style="left:930px" width="14" height="16" viewBox="0 0 14 16"><path d="M4 2l6 6-6 6" stroke="#fff" stroke-width="2.5" fill="none"/></svg>
  <div class="dots"><span></span><span class="on"></span><span></span><span></span></div>
</section>

<section class="section blog">
  <h2 class="sec-title">Latest Blog Posts</h2>
  <p class="sec-sub">Duis aute irure dolor in reprehenderit in voluptate velit esse cillum dolore eu fugiat nulla pariatur. Excepteur sint occaecat cupidatat non proident.</p>

  <article class="post" style="left:162px">
    <div class="thumb" role="img" aria-label="Illustration of a woman presenting cloud connectivity" style="background:linear-gradient(180deg,#2fa8e0,#1c7fc4)"></div>
    <div class="avatar" role="img" aria-label="Author portrait placeholder"></div>
    <h3>Sed ut perspiciatis unde omnis iste natus error sit</h3>
    <p>Lorem ipsum dolor sit amet, consectetur adipiscing elit, sed do eiusmod tempor</p>
    <span class="date"><svg width="14" height="14" viewBox="0 0 14 14"><rect x="1" y="2" width="12" height="11" fill="#f0141e"/><rect x="3" y="6" width="8" height="5" fill="#fff"/></svg>15 May 2019</span>
  </article>
  <article class="post" style="left:459px">
    <div class="thumb" role="img" aria-label="Illustration of people working around connected cloud gears" style="background:linear-gradient(180deg,#7fd8e6,#49bcd0)"></div>
    <div class="avatar" role="img" aria-label="Author portrait placeholder"></div>
    <h3>Sed ut perspiciatis unde omnis iste natus error sit</h3>
    <p>Lorem ipsum dolor sit amet, consectetur adipiscing elit, sed do eiusmod tempor</p>
    <span class="date"><svg width="14" height="14" viewBox="0 0 14 14"><rect x="1" y="2" width="12" height="11" fill="#f0141e"/><rect x="3" y="6" width="8" height="5" fill="#fff"/></svg>15 May 2019</span>
  </article>
  <article class="post" style="left:758px">
    <div class="thumb" role="img" aria-label="Illustration of a person at a laptop with network nodes" style="background:linear-gradient(180deg,#2b2a8c,#1a1960)"></div>
    <div class="avatar" role="img" aria-label="Author portrait placeholder"></div>
    <h3>Sed ut perspiciatis unde omnis iste natus error sit</h3>
    <p>Lorem ipsum dolor sit amet, consectetur adipiscing elit, sed do eiusmod tempor</p>
    <span class="date"><svg width="14" height="14" viewBox="0 0 14 14"><rect x="1" y="2" width="12" height="11" fill="#f0141e"/><rect x="3" y="6" width="8" height="5" fill="#fff"/></svg>15 May 2019</span>
  </article>
  <span class="btn">View All Blog Post &#8250;</span>
</section>

<section class="section contact">
  <h2 class="sec-title">Contact Us</h2>
  <p class="sec-sub">Duis aute irure dolor in reprehenderit in voluptate velit esse cillum dolore eu fugiat nulla pariatur. Excepteur sint occaecat cupidatat non proident.</p>
  <div class="red-band"></div>
  <div class="form">
    <div class="field" style="left:35px;top:30px;width:250px">Your Name</div>
    <div class="field" style="left:295px;top:30px;width:250px">Email</div>
    <div class="field" style="left:35px;top:76px;width:510px">Phone</div>
    <div class="field" style="left:35px;top:122px;width:510px;height:125px">Message</div>
    <div class="send">SEND &#8594;</div>
  </div>
  <div class="map" role="img" aria-label="Street map showing the office location">
    <span class="tab" style="left:8px">Map</span><span class="tab" style="left:48px;color:#888">Satellite</span>
  </div>

  <div class="info" style="left:162px">
    <span class="ring"><svg width="16" height="18" viewBox="0 0 16 18"><path d="M8 1a6 6 0 0 0-6 6c0 5 6 10 6 10s6-5 6-10a6 6 0 0 0-6-6z" fill="none" stroke="#fff" stroke-width="1.8"/><circle cx="8" cy="7" r="2" fill="#fff"/></svg></span>
    <h4>Address:</h4>27E Lorem Ipsum, State St,<br>Dummod Tempor,<br>00 01001
  </div>
  <div class="info" style="left:462px">
    <span class="ring"><svg width="18" height="14" viewBox="0 0 18 14"><rect x="1" y="1" width="16" height="12" fill="none" stroke="#fff" stroke-width="1.8"/><path d="M1 1l8 7 8-7" fill="none" stroke="#fff" stroke-width="1.8"/></svg></span>
    <h4>E-mail:</h4>info@plumvista.com<br>contact@plumvista.com
  </div>
  <div class="info" style="left:760px">
    <span class="ring"><svg width="16" height="16" viewBox="0 0 16 16"><path d="M3 1l3 0 1 4-2 1a9 9 0 0 0 5 5l1-2 4 1v3c0 1-1 2-2 2A13 13 0 0 1 1 3c0-1 1-2 2-2z" fill="#fff"/></svg></span>
    <h4>Phone:</h4>Office Number +61 3 5550 0142<br>Mobile Number +61 400 555 218
  </div>
</section>

<footer class="section footer">
  <div class="wordmark">Plumvista</div>
  <p class="about-text">Lorem ipsum dolor sit amet, consectetur adipiscing elit, sed do eiusmod tempor incididunt ut labore et dolore magna aliqua enim ad minim.</p>
  <div class="social"><span></span><span></span><span></span><span></span></div>

  <div class="fcol" style="left:460px"><h4>QUICK LINKS</h4><ul>
    <li class="current">Home</li><li>Our Services</li><li>About</li><li>Features</li><li>Our Clients</li><li>Contact</li></ul></div>
  <div class="fcol" style="left:612px"><h4>OUR SERVICES</h4><ul>
    <li>System Support</li><li>Dedicated Servers</li><li>Cloud Services</li><li>Security</li><li>Backup &amp; Restore</li><li>Network</li></ul></div>
  <div class="fcol" style="left:835px;width:205px"><h4>NEWSLETTER</h4>Subscribe to our newsletter to get latest news and updates.</div>
  <div class="news-input">Enter your email</div>

  <div class="bottom-bar"><span>&copy; Copyright Plumvista 2019 | Privacy Policy | Terms of Use</span></div>
</footer>

</body>
</html>
```